Health care technology software systems

We have a solid logo. We have company colors that will need to be used as well. We just need a great business card design. We sell to health plans but want to be modern
Updates

Need extra days to review

Target Market(s)

Health technology sector selling into Health Plans

Industry/Entity Type

Health Care Technology

Contact Information for Business Card

Name, title, address, phone number, email

Requirements
Must have
• Use of Kembrata corporate colors - Uploaded w/ our logos

```html
<!DOCTYPE html>
<html lang="en">
<head>
<meta charset="utf-8">
<title>Kembrata Business Card</title>
<link rel="stylesheet" href="https://fonts.googleapis.com/css2?family=Montserrat:wght@300;400;700&display=swap">
<style>
  :root {
    --backdrop: #3b3b3b;
    --card: #141414;
    --brand-blue: #1aa3e0;
    --brand-green: #7ac143;
    --brand-navy: #3b5aa8;
    --text-light: #f2f2f2;
  }
  * { box-sizing: border-box; margin: 0; padding: 0; }
  html, body {
    width: 1200px;
    height: 801px;
    overflow: hidden;
    background: var(--backdrop);
    font-family: "Montserrat", sans-serif;
  }
  .sheet {
    width: 1200px;
    height: 801px;
    display: flex;
    align-items: center;
    justify-content: center;
    gap: 40px;
  }
  .card {
    position: relative;
    width: 540px;
    height: 309px;
    background: var(--card);
    border-bottom: 3px solid var(--brand-blue);
    border-left: 3px solid var(--brand-blue);
    box-shadow: 0 18px 40px rgba(0,0,0,0.45);
  }
  .wordmark {
    display: flex;
    align-items: center;
    gap: 14px;
    color: var(--text-light);
    font-weight: 300;
    letter-spacing: 1px;
  }
  .wordmark .dot {
    border-radius: 50%;
    background: var(--brand-green);
    flex: none;
  }
  /* contact side */
  .card--contact .wordmark {
    position: absolute;
    left: 42px;
    top: 128px;
    font-size: 40px;
  }
  .card--contact .wordmark .dot { width: 30px; height: 30px; }
  .divider {
    position: absolute;
    left: 300px;
    top: 62px;
    width: 2px;
    height: 180px;
    background: var(--brand-blue);
  }
  .details {
    position: absolute;
    left: 318px;
    top: 66px;
    color: var(--text-light);
    font-size: 13px;
    line-height: 19px;
    font-weight: 400;
  }
  .details .name {
    color: var(--brand-blue);
    font-weight: 700;
    font-size: 17px;
    letter-spacing: 0.5px;
    line-height: 22px;
  }
  .details .row {
    display: flex;
    align-items: center;
    gap: 6px;
  }
  .details .row svg { width: 11px; height: 11px; flex: none; }
  .details .gap { height: 6px; }
  /* logo side */
  .card--logo {
    display: flex;
    align-items: center;
    justify-content: center;
  }
  .card--logo .wordmark { font-size: 60px; gap: 20px; }
  .card--logo .wordmark .dot { width: 46px; height: 46px; }
</style>
</head>
<body>
<main class="sheet">
  <section class="card card--contact">
    <div class="wordmark"><span class="dot"></span><span class="wordmark-text">kembrata</span></div>
    <div class="divider"></div>
    <div class="details">
      <p class="name">OWEN HARLOW</p>
      <p class="title">President</p>
      <p>18430 Harbor Crest</p>
      <p>Seacliff CA 92651</p>
      <div class="gap"></div>
      <p class="row">
        <svg viewBox="0 0 12 12" aria-hidden="true"><path d="M2.5 1 L4.5 1 L5.3 3.4 L4 4.4 Q5 6.8 7.6 8 L8.6 6.7 L11 7.5 L11 9.5 Q11 11 9.5 11 Q1 10.3 1 2.5 Q1 1 2.5 1Z" fill="#7ac143"/></svg>
        555-318-7702
      </p>
      <p class="row">
        <svg viewBox="0 0 12 12" aria-hidden="true"><rect x="0.5" y="2.5" width="11" height="7" fill="#7ac143"/><path d="M0.5 2.5 L6 7 L11.5 2.5" fill="none" stroke="#141414" stroke-width="1"/></svg>
        oharlow@kembrata.com
      </p>
      <p class="row">
        <svg viewBox="0 0 12 12" aria-hidden="true"><circle cx="6" cy="6" r="5.2" fill="none" stroke="#7ac143" stroke-width="1.2"/><ellipse cx="6" cy="6" rx="2.2" ry="5.2" fill="none" stroke="#7ac143" stroke-width="1"/><line x1="0.8" y1="6" x2="11.2" y2="6" stroke="#7ac143" stroke-width="1"/></svg>
        www.kembrata.com
      </p>
    </div>
  </section>
  <section class="card card--logo">
    <div class="wordmark"><span class="dot"></span><span class="wordmark-text">kembrata</span></div>
  </section>
</main>
</body>
</html>
```